Retail Package for Ammunition Company

We are looking for a packaging design for a retail boxed ammunition. The "look". Attached will be the logo to be used. The logo is attached and a can be manipulated on the box. Box to represent strength and accuracy. Will need to provide .psd files to allow in house personnel to add/remove text to other calibers and warnings. Wow me with your designs!

Browse Other Brands: http://www.brightfalconstore.com/brands

The packaging needs to include:
Logo- provided and the following text:

FRONT 1. 9mm 115gr FMJ

BACK 2. WARNING: To avoid serious injury: (1) use only ammunition in good condition; use only in modern firearms in good condition marked for .22 Long Rifle (LR) cartridges; (2) always be sure barrel is free of any obstructions; the barrel should be checked in case of light recoil, or an unusually loud or weak sound heard during firing; (3) wear eye and ear protection; (4) if gun fails to fire, avoid exposure to breech when unloading and point muzzle in a safe direction. Keep firearm pointed in safe direction at all times; (5) discharge may occur if rim is struck; handle with caution, do not drop. (6) Do not shoot at hard surfaces or water to prevent ricochet; (7) Bullet is capable of traveling extreme distances. Know your backstop; (8) Store in cool dry place

3. LEAD WARNING: Discharging firearms in poorly ventilated areas, cleaning firearms, or handling ammunition may result in exposure to lead and other substances known to cause birth defects, reproductive harm, and other serious physical injury. Have adequate ventilation at all times. Wash hands thoroughly after exposure.

Dimensions ; (LxWxH): 5.25" x 2.625" x 1.125"

Target Market(s)

Ammunition Industry

```html
<!DOCTYPE html>
<html lang="en">
<head>
<meta charset="utf-8">
<title>Iron Kestrel Supply – 1.9mm 115gr FMJ Retail Box</title>
<link href="https://fonts.googleapis.com/css2?family=Graduate&display=swap" rel="stylesheet">
<style>
  :root {
    --stage: #3a3a3a;
    --red-deep: #5e0000;
    --red-mid: #a30000;
    --red-bright: #d40a0a;
    --steel-light: #e9ebee;
    --steel-mid: #b9bec4;
    --steel-dark: #8d9299;
    --brand-red: #c8151b;
    --edge: #2a0000;
  }
  * { margin: 0; padding: 0; box-sizing: border-box; }
  html, body { width: 1200px; height: 900px; overflow: hidden; }
  body {
    background: var(--stage);
    font-family: "Graduate", "Rockwell", serif;
    display: flex; flex-direction: column; align-items: center; justify-content: center;
    gap: 28px;
  }
  .panel {
    position: relative; width: 1000px; overflow: hidden;
    border: 2px solid var(--edge);
    box-shadow: 0 10px 30px rgba(0,0,0,.45);
  }
  .hex-field {
    position: absolute; inset: 0;
    background: radial-gradient(ellipse at 55% 45%, var(--red-bright) 0%, var(--red-mid) 45%, var(--red-deep) 100%);
  }
  .lid { height: 500px; }
  .steel-flap { position: absolute; inset: 0; width: 100%; height: 100%; }
  .brand {
    position: absolute; left: 0; right: 0; top: 70px;
    display: flex; align-items: center; justify-content: center; gap: 16px;
    color: var(--brand-red);
  }
  .brand-dot { width: 26px; height: 26px; border-radius: 50%; background: var(--brand-red); }
  .brand-name { font-size: 44px; letter-spacing: 2px; }
  .spec {
    color: var(--steel-light);
    text-shadow: 0 2px 0 var(--steel-dark), 0 4px 6px rgba(0,0,0,.6);
    letter-spacing: 3px; white-space: nowrap;
  }
  .spec small { font-size: .6em; }
  .lid .spec {
    position: absolute; left: 0; right: 0; bottom: 50px; text-align: center; font-size: 86px;
  }
  .side { height: 214px; display: flex; align-items: center; }
  .emblem {
    position: relative; margin-left: 60px; width: 140px; height: 140px; border-radius: 50%;
    background: linear-gradient(135deg, var(--steel-light), var(--steel-dark));
  }
  .side .spec { position: relative; margin-left: 60px; font-size: 84px; }
</style>
</head>
<body>
  <section class="panel lid" aria-label="Box lid">
    <div class="hex-field" role="img" aria-label="Red honeycomb texture background"></div>
    <svg class="steel-flap" viewBox="0 0 1000 500" preserveAspectRatio="none" aria-hidden="true">
      <defs>
        <linearGradient id="steel" x1="0" y1="0" x2="1" y2="1">
          <stop offset="0" stop-color="#d7dadf"/>
          <stop offset=".45" stop-color="#f2f3f5"/>
          <stop offset=".7" stop-color="#b9bec4"/>
          <stop offset="1" stop-color="#9ea3aa"/>
        </linearGradient>
      </defs>
      <polygon points="0,0 1000,0 1000,130 500,260 0,130" fill="url(#steel)"/>
      <polyline points="0,130 500,260 1000,130" fill="none" stroke="#ffffff" stroke-opacity=".7" stroke-width="3"/>
    </svg>
    <div class="brand">
      <span class="brand-dot"></span>
      <span class="brand-name">IRON KESTREL SUPPLY</span>
    </div>
    <p class="spec">1.9<small>MM</small> 115<small>GR</small> FMJ</p>
  </section>

  <section class="panel side" aria-label="Box side">
    <div class="hex-field" role="img" aria-label="Red honeycomb texture background"></div>
    <div class="emblem"></div>
    <p class="spec">1.9<small>MM</small> 115<small>GR</small> FMJ</p>
  </section>
</body>
</html>
```